Front signage

Our work consists of Industrial Electrical Automation.
We are an established company with a logo we are happy with.
Though we still need:
- a sign for our front door - 420mm x 1200mm
- a sign at the front of the building - 250mm x 1600mm

Please see attached our logo, and following our colour theme would be nice, but not essential.
Please see our website for more information on what we do
www.voltarinsystems.com.au

```html
<!DOCTYPE html>
<html lang="en">
<head>
<meta charset="utf-8">
<title>Voltarin Industrial Systems – Front Signage</title>
<link href="https://fonts.googleapis.com/css2?family=Archivo+Black&family=League+Gothic&family=Roboto:wght@500&display=swap" rel="stylesheet">
<style>
  :root {
    --brand-blue: #004c99;
    --plate-edge: #0f6fd0;
    --brand-grey: #55555a;
    --brand-orange: #f55a0a;
    --panel-top: #d8d8d8;
    --panel-mid: #ffffff;
    --panel-bottom: #bcb0bf;
    --shadow: #0d1117;
    --white: #ffffff;
  }
  html, body {
    margin: 0;
    padding: 0;
    width: 1200px;
    height: 420px;
    overflow: hidden;
    background: #ffffff;
  }
  .sign {
    position: relative;
    width: 1200px;
    height: 420px;
    overflow: hidden;
  }
  .sign__backdrop {
    position: absolute;
    inset: 0;
  }
  .brand-mark {
    position: absolute;
    left: 0;
    width: 1200px;
    top: 40px;
    display: flex;
    justify-content: center;
    align-items: center;
    gap: 14px;
  }
  .brand-mark__name {
    font-family: "Archivo Black", sans-serif;
    font-size: 118px;
    line-height: 1;
    color: var(--brand-grey);
    letter-spacing: 2px;
  }
  .brand-mark__dot {
    width: 26px;
    height: 26px;
    border-radius: 50%;
    background: var(--brand-orange);
  }
  .company-name {
    position: absolute;
    left: 0;
    width: 1200px;
    top: 256px;
    margin: 0;
    text-align: center;
    font-family: "Archivo Black", sans-serif;
    font-weight: 400;
    font-size: 43px;
    line-height: 1;
    letter-spacing: 0.5px;
    color: var(--brand-grey);
    white-space: nowrap;
  }
  .company-name__accent { color: var(--brand-blue); }
  .tagline {
    position: absolute;
    left: 200px;
    width: 800px;
    top: 316px;
    display: flex;
    align-items: center;
    justify-content: space-between;
    gap: 16px;
  }
  .tagline__rule {
    flex: 1;
    height: 2px;
    background: var(--brand-orange);
  }
  .tagline__text {
    font-family: "Roboto", sans-serif;
    font-weight: 500;
    font-size: 17px;
    letter-spacing: 2.6px;
    color: var(--brand-orange);
    white-space: nowrap;
  }
  .services {
    position: absolute;
    left: 184px;
    width: 834px;
    top: 360px;
    height: 50px;
    margin: 0;
    padding: 0;
    list-style: none;
    background: var(--brand-blue);
    display: flex;
    flex-wrap: nowrap;
    justify-content: center;
    align-items: center;
    font-family: "League Gothic", sans-serif;
    font-weight: 400;
    font-size: 27px;
    line-height: 1;
    color: var(--white);
    letter-spacing: 0.2px;
    white-space: nowrap;
    overflow: hidden;
  }
  .services__item {
    flex: 0 0 auto;
    white-space: nowrap;
  }
  .services__item + .services__item::before {
    content: "•";
    color: var(--brand-orange);
    margin: 0 7px;
  }
</style>
</head>
<body>
<main class="sign">
  <svg class="sign__backdrop" width="1200" height="420" viewBox="0 0 1200 420" xmlns="http://www.w3.org/2000/svg">
    <defs>
      <linearGradient id="plateGradient" x1="0" y1="0" x2="1" y2="1">
        <stop offset="0" stop-color="#0b3a74"/>
        <stop offset="0.5" stop-color="#0c4587"/>
        <stop offset="1" stop-color="#083468"/>
      </linearGradient>
      <linearGradient id="panelGradient" x1="0" y1="0" x2="0" y2="1">
        <stop offset="0" stop-color="#d8d8d8"/>
        <stop offset="0.45" stop-color="#ffffff"/>
        <stop offset="0.75" stop-color="#eeeaee"/>
        <stop offset="1" stop-color="#bcb0bf"/>
      </linearGradient>
    </defs>
    <rect class="plate" role="img" aria-label="Blue diamond tread steel plate texture" x="0" y="0" width="1200" height="420" fill="url(#plateGradient)"/>
    <polygon class="panel-shadow" points="255,0 945,0 1112,210 945,420 255,420 88,210" fill="#0d1117"/>
    <polygon class="panel-edge" points="268,0 932,0 1112,210 932,420 268,420 88,210" fill="#0f6fd0"/>
    <polygon class="panel" points="272,0 928,0 1106,210 928,420 272,420 94,210" fill="url(#panelGradient)"/>
  </svg>

  <div class="brand-mark">
    <span class="brand-mark__name">VIS</span>
    <span class="brand-mark__dot"></span>
  </div>

  <h1 class="company-name">VOLTARIN <span class="company-name__accent">INDUSTRIAL</span> SYSTEMS</h1>

  <div class="tagline">
    <span class="tagline__rule"></span>
    <span class="tagline__text">INDUSTRIAL ELECTRICAL AND MECHANICAL SERVICES</span>
    <span class="tagline__rule"></span>
  </div>

  <ul class="services">
    <li class="services__item">COMMUNICATIONS</li>
    <li class="services__item">ELECTRICAL INDUSTRIAL AUTOMATION</li>
    <li class="services__item">WATER JET CUTTING</li>
    <li class="services__item">MCC PANEL BUILDING</li>
  </ul>
</main>
</body>
</html>
```